Graphics for Vorlani telehealth weight loss plans

Vorlani focuses on delivering medical weight-loss using prescription medicine and telehealth consults. Vorlani needs graphics for its ecommerce site for three weight loss plans. The plans are posted here with current graphics and descriptions of what is included with each plan. Please do not feel constrained by current graphics or styling.

- https://shop.vorlanicare.com/products/steady-horizon-plan
- https://shop.vorlanicare.com/products/amber-ridge-plan
- https://shop.vorlanicare.com/products/calm-harbor-plan

The graphics need to look good on mobile and desktop browsers.

```html
<!DOCTYPE html>
<html lang="en">
<head>
<meta charset="utf-8">
<title>Vorlani Weight Loss Plans</title>
<link rel="stylesheet" href="https://fonts.googleapis.com/css2?family=Arimo:wght@700&family=Jost:wght@500&family=Montserrat:wght@700&display=swap">
<style>
  :root {
    --canvas: #000000;
    --brand-teal: #1f5f78;
    --silver-light: #f4f4f4;
    --silver-mid: #c9c9c9;
    --text-light: #ffffff;
    --amber-deep: #163f66;
    --amber-mid: #2a5b86;
    --harbor-deep: #112b3a;
    --harbor-warm: #6d6252;
    --horizon-warm: #8a7d6f;
    --horizon-deep: #173645;
  }
  * { margin: 0; padding: 0; box-sizing: border-box; }
  html, body {
    width: 1200px; height: 580px; overflow: hidden;
    background: var(--canvas);
  }
  .plan-row { position: relative; width: 1200px; height: 580px; }
  .plan-card {
    position: absolute; top: 98px; width: 292px; height: 378px; overflow: hidden;
  }
  .plan-card--amber { left: 90px; }
  .plan-card--harbor { left: 454px; }
  .plan-card--horizon { left: 818px; }

  .plan-header {
    height: 93px;
    display: flex; align-items: center; justify-content: center;
    background: linear-gradient(180deg, var(--silver-light) 0%, var(--silver-mid) 50%, var(--silver-light) 100%);
  }
  .brand-name {
    font-family: "Jost", sans-serif; font-weight: 500;
    font-size: 30px; letter-spacing: 1px; color: var(--brand-teal);
  }

  .plan-body { position: relative; height: 285px; }
  .plan-photo { position: absolute; inset: 0; }
  .plan-card--amber .plan-photo {
    background: radial-gradient(circle at 65% 60%, var(--amber-mid), var(--amber-deep) 75%);
  }
  .plan-card--harbor .plan-photo {
    background: linear-gradient(200deg, var(--harbor-deep) 40%, var(--harbor-warm) 100%);
  }
  .plan-card--horizon .plan-photo {
    background: linear-gradient(160deg, var(--horizon-warm) 10%, var(--horizon-deep) 90%);
  }

  .plan-title {
    position: absolute; left: 17px; top: 14px;
    font-family: "Arimo", sans-serif; font-weight: 700;
    font-size: 34px; line-height: 39px; color: var(--text-light);
    text-shadow: 1px 2px 3px rgba(0,0,0,0.45);
  }
  .billing-icon {
    position: absolute; left: 114px; top: 150px; width: 64px; height: 66px;
    filter: drop-shadow(1px 2px 2px rgba(0,0,0,0.5));
  }
  .billing-terms {
    position: absolute; left: 0; right: 0; top: 222px;
    text-align: center;
    font-family: "Montserrat", sans-serif; font-weight: 700;
    font-size: 14px; line-height: 17px; color: var(--text-light);
    text-shadow: 1px 1px 2px rgba(0,0,0,0.6);
  }
</style>
</head>
<body>
<main class="plan-row">

  <article class="plan-card plan-card--amber">
    <header class="plan-header"><span class="brand-name">Vorlani</span></header>
    <div class="plan-body">
      <div class="plan-photo" role="img" aria-label="Prescription bottle tipped over with capsules spilling onto a wooden table, toned blue"></div>
      <h2 class="plan-title">Amber<br>Ridge<br>Plan</h2>
      <svg class="billing-icon" viewBox="0 0 64 66" aria-hidden="true">
        <g fill="none" stroke="#fff" stroke-width="4" stroke-linecap="round">
          <path d="M36 4 A29 29 0 0 1 48 58"/>
          <path d="M28 62 A29 29 0 0 1 16 8"/>
        </g>
        <path d="M28 0 L38 4 L30 11 Z M36 66 L26 62 L34 55 Z" fill="#fff"/>
        <rect x="17" y="19" width="30" height="28" rx="4" fill="none" stroke="#fff" stroke-width="3"/>
        <line x1="17" y1="27" x2="47" y2="27" stroke="#fff" stroke-width="3"/>
        <g fill="#fff"><rect x="22" y="15" width="3" height="7"/><rect x="39" y="15" width="3" height="7"/>
          <rect x="21" y="31" width="4" height="4"/><rect x="27" y="31" width="4" height="4"/><rect x="33" y="31" width="4" height="4"/><rect x="39" y="31" width="4" height="4"/>
          <rect x="21" y="38" width="4" height="4"/><rect x="27" y="38" width="4" height="4"/><rect x="33" y="38" width="4" height="4"/><rect x="39" y="38" width="4" height="4"/></g>
      </svg>
      <p class="billing-terms">MONTH TO MONTH<br>PAY AS YOU GO</p>
    </div>
  </article>

  <article class="plan-card plan-card--harbor">
    <header class="plan-header"><span class="brand-name">Vorlani</span></header>
    <div class="plan-body">
      <div class="plan-photo" role="img" aria-label="Meal-prep container of roasted vegetables and meat, toned dark teal"></div>
      <h2 class="plan-title">Calm<br>Harbor<br>Plan</h2>
      <svg class="billing-icon" viewBox="0 0 64 66" aria-hidden="true">
        <g fill="none" stroke="#fff" stroke-width="4" stroke-linecap="round">
          <path d="M36 4 A29 29 0 0 1 48 58"/>
          <path d="M28 62 A29 29 0 0 1 16 8"/>
        </g>
        <path d="M28 0 L38 4 L30 11 Z M36 66 L26 62 L34 55 Z" fill="#fff"/>
        <rect x="17" y="19" width="30" height="28" rx="4" fill="none" stroke="#fff" stroke-width="3"/>
        <line x1="17" y1="27" x2="47" y2="27" stroke="#fff" stroke-width="3"/>
        <g fill="#fff"><rect x="22" y="15" width="3" height="7"/><rect x="39" y="15" width="3" height="7"/>
          <rect x="21" y="31" width="4" height="4"/><rect x="27" y="31" width="4" height="4"/><rect x="33" y="31" width="4" height="4"/><rect x="39" y="31" width="4" height="4"/>
          <rect x="21" y="38" width="4" height="4"/><rect x="27" y="38" width="4" height="4"/><rect x="33" y="38" width="4" height="4"/><rect x="39" y="38" width="4" height="4"/></g>
      </svg>
      <p class="billing-terms">MONTH TO MONTH<br>PAY AS YOU GO</p>
    </div>
  </article>

  <article class="plan-card plan-card--horizon">
    <header class="plan-header"><span class="brand-name">Vorlani</span></header>
    <div class="plan-body">
      <div class="plan-photo" role="img" aria-label="Close-up of a toned torso, warm skin tones fading to teal"></div>
      <h2 class="plan-title">Steady<br>Horizon<br>Plan</h2>
      <svg class="billing-icon" viewBox="0 0 64 66" aria-hidden="true">
        <g fill="none" stroke="#fff" stroke-width="4" stroke-linecap="round">
          <path d="M36 4 A29 29 0 0 1 48 58"/>
          <path d="M28 62 A29 29 0 0 1 16 8"/>
        </g>
        <path d="M28 0 L38 4 L30 11 Z M36 66 L26 62 L34 55 Z" fill="#fff"/>
        <rect x="17" y="19" width="30" height="28" rx="4" fill="none" stroke="#fff" stroke-width="3"/>
        <line x1="17" y1="27" x2="47" y2="27" stroke="#fff" stroke-width="3"/>
        <g fill="#fff"><rect x="22" y="15" width="3" height="7"/><rect x="39" y="15" width="3" height="7"/>
          <rect x="21" y="31" width="4" height="4"/><rect x="27" y="31" width="4" height="4"/><rect x="33" y="31" width="4" height="4"/><rect x="39" y="31" width="4" height="4"/>
          <rect x="21" y="38" width="4" height="4"/><rect x="27" y="38" width="4" height="4"/><rect x="33" y="38" width="4" height="4"/><rect x="39" y="38" width="4" height="4"/></g>
      </svg>
      <p class="billing-terms">MONTH TO MONTH<br>PAY AS YOU GO</p>
    </div>
  </article>

</main>
</body>
</html>
```